A parent Company needs a website as a leading diversified business in industrial Conglomerates in Af

Tesku Group is a private (Holding) limited liability company incorporated under the Companies Code, 1963 (Act 179) in November, 2013 to following the speedy growth in numbers of its current subsidiaries which has been founded several years ago with an emerging force to become one of the largest and a leading diversified business in industrial Conglomerates in Africa.
The Group which is 100% wholly owned indigenous Ghanaian Company focuses on provision of local, value-added products and services that meet the needs of the African population. The Group is headquartered in Accra, Ghana with interests across a range of sectors in Africa.
We are currently into Food & Beverage, Real Estate Development, Transportation, Health Care, Consumer Products Distribution, Agro Processing, Manufacturing, ICT, Exports & Import, and still counting.
In the next 3 years, we shall announce our ambitions to enter Ghana's largest Oil and Gas industry, playing a strategic role in the petroleum sector with strategic alliances, and help build Ghana's biggest and most important Energy sector in the country.
Inspired by billionaires Ned Harlow, Colin Ashdown, and Efemi Okorusa, Tesku Group (Tesku Foundation) is committed to making a name for itself on the philanthropic circuit and has given away privately and still given to the cause to the needy in the society and some specific social causes in Ghana.
The company is managed by a 5 member board and a 2 member advisory experts who are non-board members.
The company has a vision, mission and it is guided by its core values.
We would like to see a designs that is very professional and looks corporate and can attract investors and partners. It must communicate financial safety and growth and must reflect our logo colors.

```html
<!DOCTYPE html>
<html lang="en">
<head>
<meta charset="utf-8">
<title>Tesku Group</title>
<link href="https://fonts.googleapis.com/css2?family=Roboto:ital,wght@0,400;0,500;1,400&family=Roboto+Condensed:wght@400;700&display=swap" rel="stylesheet">
<style>
:root{
  --blue:#2f8fd3;
  --blue-dark:#1f6fae;
  --navy:#1c4f86;
  --title:#1d5d96;
  --text:#555;
  --muted:#8a8a8a;
  --rule:#e2e2e2;
  --footer:#4a4a4a;
  --footer-text:#dddddd;
}
*{margin:0;padding:0;box-sizing:border-box}
html,body{width:893px;height:1200px;overflow:hidden;background:#fff}
body{position:relative;font-family:Roboto,Arial,sans-serif;color:var(--text)}
.abs{position:absolute}
.brand{left:128px;top:16px;width:84px;text-align:center}
.brand-mark{width:28px;height:28px;border-radius:50%;background:var(--blue);margin:0 auto 8px}
.brand-name{font-size:11px;color:var(--navy);letter-spacing:.3px;white-space:nowrap}
.search{left:510px;top:35px;width:143px;height:18px;border:1px solid #bdbdbd;border-radius:3px;font-size:7px;color:#999;padding:4px 9px}
.search svg{position:absolute;right:6px;top:3px}
.contact{left:675px;font-size:7.5px;color:#666;display:flex;align-items:center;gap:6px}
.nav{left:0;top:77px;width:893px;height:29px;background:linear-gradient(#3d9fe0,#2a85c9)}
.nav a{position:absolute;top:0;height:29px;line-height:29px;color:#fff;font-size:10px;text-decoration:none;transform:translateX(-50%)}
.nav .active{left:128px;width:84px;transform:none;text-align:center;background:var(--blue-dark)}
.hero{left:0;top:106px;width:893px;height:318px;background:linear-gradient(180deg,#d9c49a 0%,#c9a46a 45%,#a9772f 75%,#7b5420 100%)}
.hero h1{position:absolute;left:148px;top:180px;font-family:"Roboto Condensed",sans-serif;font-weight:400;font-size:27px;color:#222}
.hero h2{position:absolute;left:148px;top:216px;font-family:"Roboto Condensed",sans-serif;font-weight:400;font-size:21px;color:#222}
.arrow{position:absolute;top:143px;width:32px;height:32px;border:2px solid rgba(255,255,255,.5);border-radius:50%}
.center{left:0;width:893px;text-align:center}
.sec-title{font-size:14px;color:var(--title)}
.intro{left:135px;top:469px;width:623px;text-align:center;font-size:8.3px;line-height:15.5px;color:#555}
.rule{left:135px;top:527px;width:625px;height:1px;background:var(--rule)}
.tile{overflow:hidden;text-align:center;color:#fff}
.tile h3{font-family:"Roboto Condensed",sans-serif;font-weight:700;font-size:11px;margin-top:38px}
.tile p{font-size:6.8px;font-style:italic;line-height:11.5px;margin-top:6px}
.tile .more{display:inline-block;margin-top:11px;background:rgba(40,40,40,.6);font-family:"Roboto Condensed",sans-serif;font-size:8px;padding:5px 11px}
.apps-title{left:140px;top:878px;font-family:"Roboto Condensed",sans-serif;font-weight:700;font-size:12px;color:var(--title)}
.app{width:155px;height:52px;border-bottom:1px solid var(--rule)}
.app .thumb{position:absolute;left:0;top:0;width:46px;height:40px}
.app h4{position:absolute;left:56px;top:2px;font-weight:400;font-size:7.6px;color:var(--title)}
.app p{position:absolute;left:56px;top:15px;font-size:6.8px;line-height:11.5px;color:#888;width:100px}
.btn{height:25px;border-radius:3px;background:linear-gradient(#2d7fc0,#1c5d98);color:#fff;font-family:"Roboto Condensed",sans-serif;font-size:8.5px;text-align:center;line-height:25px;width:100px}
.posts-title{left:490px;top:876px;font-size:13px;color:var(--title)}
.post-photo{left:490px;top:903px;width:152px;height:207px}
.post h4{font-weight:400;font-size:10.5px;line-height:15.5px;color:var(--title)}
.post p{font-size:6.8px;line-height:11.5px;color:#888;margin-top:5px}
.footer{left:0;top:1133px;width:893px;height:67px;background:var(--footer)}
.flinks{left:130px;top:20px;font-size:7px;color:var(--footer-text);word-spacing:2px}
.copy{left:130px;top:38px;font-size:7px;color:var(--footer-text)}
.social{top:22px;width:20px;height:20px;border-radius:50%;background:#777}
</style>
</head>
<body>

<header>
  <div class="abs brand">
    <div class="brand-mark"></div>
    <div class="brand-name">TESKU GROUP</div>
  </div>
  <div class="abs search">Search :
    <svg width="11" height="11" viewBox="0 0 11 11"><circle cx="4.5" cy="4.5" r="3.5" fill="none" stroke="#888" stroke-width="1.2"/><line x1="7" y1="7" x2="10" y2="10" stroke="#888" stroke-width="1.4"/></svg>
  </div>
  <div class="abs contact" style="top:23px">
    <svg width="6" height="9" viewBox="0 0 6 9"><rect x="0.5" y="0.5" width="5" height="8" rx="1" fill="none" stroke="#555"/></svg>( 1202 ) 310 220</div>
  <div class="abs contact" style="top:41px">
    <svg width="9" height="7" viewBox="0 0 9 7"><rect width="9" height="7" fill="#666"/><path d="M0 0l4.5 4 4.5-4" stroke="#fff" fill="none" stroke-width=".8"/></svg>info@teskugroup.com</div>
</header>

<nav class="abs nav">
  <a class="active" href="#">Home</a>
  <a style="left:259px" href="#">About Us</a>
  <a style="left:353px" href="#">Services</a>
  <a style="left:453px" href="#">Testimonials</a>
  <a style="left:554px" href="#">Features</a>
  <a style="left:638px" href="#">Blog</a>
  <a style="left:720px" href="#">Contact</a>
</nav>

<section class="abs hero" role="img" aria-label="Combine harvesters working a golden wheat field">
  <span class="arrow" style="left:48px"></span>
  <span class="arrow" style="left:813px"></span>
  <h1>AGRO PROCESSING</h1>
  <h2>WE ARE INTO THESE BUSINESS VERTICALS.</h2>
</section>

<h2 class="abs center sec-title" style="top:442px;font-weight:400">Welcome to Tesku Holding Group</h2>
<p class="abs intro">Using 'Content here, content here', making it look like readable English. Many desktop publishing packages and web page editors now use Lorem Ipsum as their default model text, and a search for 'lorem ipsum' will uncover many web sites still in their infancy. Various versions have evolved over the years, sometimes by accident, sometimes on purpose</p>
<div class="abs rule"></div>
<h2 class="abs center sec-title" style="top:539px;font-weight:400">Our Features</h2>

<div class="abs tile" style="left:135px;top:572px;width:204px;height:137px;background:linear-gradient(135deg,#3a2a1c,#8a6a45 55%,#d9d2c2)" role="img" aria-label="Plated food and a glass of white wine"></div>
<div class="abs tile" style="left:346px;top:572px;width:204px;height:137px;background:linear-gradient(#3d5874,#2a3d52)" role="img" aria-label="City skyline with glass towers">
  <h3>REAL ESTATE DEVELOPMENT</h3><p>Using 'Content here, content here', making it look like<br>English. Many desktop publishing packages</p><span class="more">[ + ] READ MORE</span></div>
<div class="abs tile" style="left:557px;top:572px;width:203px;height:137px;background:linear-gradient(#5c6468,#3b4245)" role="img" aria-label="Red truck on a highway">
  <h3>TRANSPORTATION</h3><p>Using 'Content here, content here', making it look like<br>English. Many desktop publishing packages</p><span class="more">[ + ] READ MORE</span></div>
<div class="abs tile" style="left:135px;top:716px;width:204px;height:136px;background:linear-gradient(#7e8fa2,#5e6e80)" role="img" aria-label="Team of medical staff">
  <h3>HEALTH CARE</h3><p>Using 'Content here, content here', making it look like<br>English. Many desktop publishing packages</p><span class="more">[ + ] READ MORE</span></div>
<div class="abs tile" style="left:346px;top:716px;width:204px;height:136px;background:linear-gradient(#6e6862,#4a4540)" role="img" aria-label="Courier handing a parcel to a customer">
  <h3>CONSUMER PRODUCTS DISTRIBUTION</h3><p>Using 'Content here, content here', making it look like<br>English. Many desktop publishing packages</p><span class="more">[ + ] READ MORE</span></div>
<div class="abs tile" style="left:552px;top:714px;width:228px;height:140px;background:linear-gradient(#4f7eb8,#3b5f80 45%,#6a5a3a);border:1px solid #999" role="img" aria-label="Tractor on a farm field">
  <h3>AGRO PROCESSING</h3><p>Using 'Content here, content here', making it look like<br>English. Many desktop publishing packages</p><span class="more">[ + ] READ MORE</span></div>

<h2 class="abs apps-title">TOP APPS</h2>
<div class="abs app" style="left:138px;top:906px"><div class="thumb" style="background:linear-gradient(#c94a1e,#e8a23a)" role="img" aria-label="Drinks"></div><h4>Agro Processing</h4><p>It was popularised in the 1960s with the release...</p></div>
<div class="abs app" style="left:310px;top:906px"><div class="thumb" style="background:linear-gradient(#8fb2cf,#3a4652)" role="img" aria-label="Engineers on site"></div><h4>Agro Processing</h4><p>It was popularised in the 1960s with the release...</p></div>
<div class="abs app" style="left:138px;top:964px"><div class="thumb" style="background:linear-gradient(#9fc4e0,#3a6f9c)" role="img" aria-label="Fitness class"></div><h4>Agro Processing</h4><p>It was popularised in the 1960s with the release...</p></div>
<div class="abs app" style="left:310px;top:964px"><div class="thumb" style="background:linear-gradient(#6b3e22,#d9cfc0)" role="img" aria-label="Plated dish"></div><h4>Agro Processing</h4><p>It was popularised in the 1960s with the release...</p></div>
<div class="abs app" style="left:138px;top:1022px"><div class="thumb" style="background:linear-gradient(#d8d8d8,#333)" role="img" aria-label="Train"></div><h4>Agro Processing</h4><p style="left:62px">It was popularised in the 1960s with the release...</p></div>
<div class="abs app" style="left:310px;top:1022px"><div class="thumb" style="background:linear-gradient(#f0f3f6,#6aa9d6)" role="img" aria-label="Doctor"></div><h4>Agro Processing</h4><p>It was popularised in the 1960s with the release...</p></div>
<div class="abs btn" style="left:369px;top:1080px">VIEW MORE NEWS</div>

<h2 class="abs posts-title" style="font-weight:400">Recent Posts</h2>
<svg class="abs" style="left:748px;top:880px" width="16" height="8" viewBox="0 0 16 8"><path d="M4 1L1 4l3 3M12 1l3 3-3 3" fill="none" stroke="#aaa"/></svg>
<div class="abs post-photo" style="background:linear-gradient(#fff 0%,#e9ded2 20%,#8a5a34 55%,#4a3a2e 100%)" role="img" aria-label="Delivery man holding a parcel and clipboard"></div>
<div class="abs post" style="left:652px;top:907px;width:112px">
  <h4>Consumer Products Distribution</h4>
  <p>It was popularised in the 1960s with the release of Typeset sheets containing Lorem Ipsum passages, and more recently with desktop publishing passages, and more recently with desktop publishing</p>
  <p style="margin-top:11px">It was popularised in the 1960s with the release of Typeset sheets...</p>
</div>
<div class="abs btn" style="left:655px;top:1079px">VIEW MORE POSTS</div>

<footer class="abs footer">
  <div class="abs flinks">Home &nbsp;| &nbsp;About Us &nbsp;| &nbsp;Services &nbsp;| &nbsp;Testimonials &nbsp;| &nbsp;Blog &nbsp;| &nbsp;Contact</div>
  <div class="abs copy">Copyright © 2014. Tesku Holding Group. All rights reserved.</div>
  <span class="abs social" style="left:695px"></span>
  <span class="abs social" style="left:719px"></span>
  <span class="abs social" style="left:743px"></span>
</footer>

</body>
</html>
```